We need a new label.

The idea is to have Calverton Estate across the top of the label.

Then have a CE in the center of the label in the font liberty cursive capital letters.

The brand name is "Dune Gate" Shiraz

The must have across the bottom of the label are:

750ml

Wine of Australia

Note:
We are thinking a black background with silver script. (we are not married to this)
However due to the price point we can not use foil.

The ultimate goal is to present this wine as authentically Australian with a goal of presenting Australia as clean, green and friendly.

```html
<!DOCTYPE html>
<html lang="en">
<head>
<meta charset="utf-8">
<title>Calverton Estate – Dune Gate Shiraz Label</title>
<link href="https://fonts.googleapis.com/css2?family=Oswald:wght@400&family=Open+Sans:wght@700&family=Satisfy&display=swap" rel="stylesheet">
<style>
  :root {
    --backdrop-edge: #000000;
    --backdrop-centre: #2a2a2a;
    --label-bg: #333333;
    --label-frame: #ffffff;
    --ornament-dark: #050505;
    --ornament-mid: #2a2a2a;
    --gold: #dba822;
    --white: #ffffff;
    --muted: #6e6a66;
    --badge: #000000;
  }
  html, body {
    margin: 0;
    padding: 0;
    width: 919px;
    height: 1200px;
    overflow: hidden;
  }
  .canvas {
    position: relative;
    width: 919px;
    height: 1200px;
    background: linear-gradient(90deg, var(--backdrop-edge) 0%, var(--backdrop-centre) 50%, var(--backdrop-edge) 100%);
  }
  .label {
    position: absolute;
    left: 156px;
    top: 215px;
    width: 642px;
    height: 769px;
    box-sizing: border-box;
    border: 2px solid var(--label-frame);
    border-radius: 2px;
    background: var(--label-bg);
    overflow: hidden;
  }
  .wing-ornament {
    position: absolute;
    left: 0;
    top: 0;
    width: 100%;
    height: 440px;
    background:
      radial-gradient(ellipse 42% 70% at 8% 20%, var(--ornament-dark) 0%, var(--ornament-mid) 70%, transparent 100%),
      radial-gradient(ellipse 42% 70% at 92% 20%, var(--ornament-dark) 0%, var(--ornament-mid) 70%, transparent 100%);
  }
  .brand-mark {
    position: absolute;
    left: 0;
    top: 0;
    width: 642px;
    height: 480px;
  }
  .brand-name {
    font-family: "Open Sans", sans-serif;
    font-weight: 700;
    font-size: 34px;
    letter-spacing: 1px;
    fill: var(--gold);
  }
  .badge { fill: var(--badge); }
  .badge-initials {
    font-family: "Open Sans", sans-serif;
    font-weight: 700;
    font-size: 96px;
    fill: var(--gold);
  }
  .wine-name {
    position: absolute;
    left: 0;
    width: 100%;
    text-align: center;
    font-family: "Oswald", sans-serif;
    font-weight: 400;
    margin: 0;
    text-transform: uppercase;
  }
  .wine-name--product {
    top: 485px;
    font-size: 58px;
    line-height: 70px;
    color: var(--gold);
    letter-spacing: 1px;
  }
  .wine-name--variety {
    top: 560px;
    font-size: 42px;
    line-height: 52px;
    color: var(--white);
  }
  .volume {
    position: absolute;
    top: 645px;
    left: 0;
    width: 100%;
    text-align: center;
    font-family: "Satisfy", cursive;
    font-size: 44px;
    line-height: 56px;
    color: var(--white);
    margin: 0;
  }
  .origin {
    position: absolute;
    top: 727px;
    left: 0;
    width: 100%;
    text-align: center;
    font-family: "Oswald", sans-serif;
    font-size: 24px;
    line-height: 30px;
    letter-spacing: 12px;
    padding-left: 12px;
    box-sizing: border-box;
    color: var(--muted);
    margin: 0;
  }
</style>
</head>
<body>
  <main class="canvas">
    <section class="label">
      <div class="wing-ornament" role="img" aria-label="Stylised pair of wings spreading across the top of the label"></div>

      <svg class="brand-mark" viewBox="0 0 642 480" aria-label="Calverton Estate">
        <defs>
          <path id="brand-arc" d="M 167 275 A 165 165 0 0 1 477 275"/>
        </defs>
        <text class="brand-name">
          <textPath href="#brand-arc" startOffset="50%" text-anchor="middle">CALVERTON ESTATE</textPath>
        </text>
        <ellipse class="badge" cx="322" cy="331" rx="121" ry="121"/>
        <text class="badge-initials" x="322" y="365" text-anchor="middle">CE</text>
      </svg>

      <h1 class="wine-name wine-name--product">Dune Gate</h1>
      <h2 class="wine-name wine-name--variety">Shiraz</h2>
      <p class="volume">750ml</p>
      <p class="origin">WINE OF AUSTRALIA</p>
    </section>
  </main>
</body>
</html>
```